Business Card Design

Please use the Logo for colors and styles, and create a business card using the following info:

Matthias Loeber
Web Developer

Loeber Solutions
+41 76 482 17 05
matthias@loeber-solutions.example
www.loeber-solutions.example

Download the logo at http://loeber-solutions.example/tl_files/loeber_solutions.zip

Thanks for your works!

```html
<!DOCTYPE html>
<html lang="en">
<head>
<meta charset="utf-8">
<title>Loeber Solutions – Business Card</title>
<link rel="stylesheet" href="https://fonts.googleapis.com/css2?family=Questrial&family=Mulish:wght@400;700&display=swap">
<style>
  :root {
    --page-bg: #ecebe8;
    --card-white: #ffffff;
    --brand-blue: #2f6fa8;
    --name-blue: #2f5377;
    --text-blue: #1f3d5c;
    --muted-blue: #4f6a85;
    --back-light: #3d6b94;
    --back-dark: #0c426f;
    --label-grey: #8a8d91;
  }
  * { margin: 0; padding: 0; box-sizing: border-box; }
  html, body {
    width: 1200px;
    height: 900px;
    overflow: hidden;
    background: var(--page-bg);
  }
  .sheet {
    position: relative;
    width: 1200px;
    height: 900px;
  }
  .card {
    position: absolute;
    top: 341px;
    width: 438px;
    height: 244px;
    box-shadow: 0 2px 6px rgba(0, 0, 0, 0.18);
  }
  .card--front {
    left: 67px;
    background: var(--card-white);
  }
  .card--back {
    left: 680px;
    background: linear-gradient(115deg, var(--back-light) 0%, #2a5a85 40%, var(--back-dark) 75%, #1f5683 100%);
  }
  .wordmark {
    position: absolute;
    font-family: "Questrial", sans-serif;
    font-size: 37px;
    letter-spacing: 0.5px;
    line-height: 1;
    white-space: nowrap;
  }
  .card--front .wordmark {
    left: 18px;
    top: 42px;
    color: var(--brand-blue);
  }
  .card--back .wordmark {
    left: 0;
    right: 0;
    top: 42px;
    text-align: center;
    color: #ffffff;
  }
  .address {
    position: absolute;
    left: 19px;
    top: 95px;
    font-family: "Mulish", sans-serif;
    font-size: 14.5px;
    color: var(--muted-blue);
  }
  .person {
    position: absolute;
    left: 20px;
    top: 154px;
    font-family: "Mulish", sans-serif;
  }
  .person__name {
    font-size: 20px;
    font-weight: 700;
    color: var(--name-blue);
    line-height: 1.2;
  }
  .person__role {
    font-size: 15px;
    color: var(--muted-blue);
    margin-top: 2px;
  }
  .contact {
    position: absolute;
    left: 220px;
    top: 154px;
    font-family: "Mulish", sans-serif;
    font-size: 14.5px;
    line-height: 19px;
    color: var(--text-blue);
    list-style: none;
  }
  .side-label {
    position: absolute;
    top: 632px;
    font-family: "Mulish", sans-serif;
    font-size: 40px;
    color: var(--label-grey);
    letter-spacing: 1px;
  }
  .side-label--front { left: 360px; }
  .side-label--back { left: 980px; }
</style>
</head>
<body>
<main class="sheet">
  <section class="card card--front" aria-label="Card front">
    <p class="wordmark">LOEBER SOLUTIONS</p>
    <p class="address">Birkenweg 14, CH-8600 Talwil</p>
    <div class="person">
      <p class="person__name">Matthias Loeber</p>
      <p class="person__role">Web Developer</p>
    </div>
    <ul class="contact">
      <li>+41 76 482 17 05</li>
      <li>matthias@loeber-solutions.example</li>
      <li>www.loeber-solutions.example</li>
    </ul>
  </section>
  <p class="side-label side-label--front">FRONT</p>

  <section class="card card--back" aria-label="Card back">
    <p class="wordmark">LOEBER SOLUTIONS</p>
  </section>
  <p class="side-label side-label--back">BACK</p>
</main>
</body>
</html>
```